Guitar parts retail packaging

I have 2 boxes I need designed. This will be for my guitar parts. They are going to be thick cardstock type paper box, with a foam insert to secure the items. Matte finish with silver foil printing is sort of where im headed, but Im open to other beautiful design. The boxes will need to have a window on top of the box to show the product inside. Color scheme Im thinking with is Black with red, white and Silver foil printing. Unless you come up with something nicer, im open to that. But my business cards and some stickers are those colors.
2 different size boxes, but they can be the same basic design, modified for 2 different sizes. They will open at the front, and the lid will lift, hinged at the top back edge. (Please see purple box in picture for example for how box will work). Both boxes will have a window on top to showcase product in the box. One of the sides, (2" X 1.25") will be left a solid color, grey or other so I can put a product sticker on that side to designate what type of product is in the box. So you are really just designing the top (With window), front, back, and 1 side. Maybe something clever on the bottom but if thats blank thats fine.
LARGE BOX:
5.25 wide (Left to right)
2” deep (Front to back)
1.25” tall (Top to bottom)
SMALL BOX:
2” Wide (Left to right)
2” Deep (Front to back)
Please see Business card and sticker in picture for color scheme Im thinking. ( I am open to other colors and designs as well)

Target Market(s)

Musicians, Rockers, tattoo junkies, general badasses.

Industry/Entity Type

Guitar industry. Rock & Rollers

Font styles to use
Other font styles liked:
• I use a font called Morpheus for my logo. Also Times New Roman, maybe Copperplate? Or something more creative? Im open as long as it fits.

Colors
EB3D1F
EC4F4E
F09395
F8D3D4
FCEDEE

Requirements
Must have
• My Company name and logo (Hollow Marigold). Also slogan-
Nice to have
• Please see general aesthetic in sticker and biz card.
Should not have
• No horror themes, keep it cool and classy. (Even though logo is a skull). And please no pictures of guitars on the box. You might add a pic of 1 type of guitar, but the parts inside might not fit that guitar pictured on the box.

```html
<!DOCTYPE html>
<html lang="en">
<head>
<meta charset="utf-8">
<title>Hollow Marigold – Guitar Parts Box</title>
<link href="https://fonts.googleapis.com/css2?family=Cinzel:wght@500&display=swap" rel="stylesheet">
<style>
  :root {
    --backdrop: #d8d6d8;
    --box-red: #c4161f;
    --box-red-deep: #a9121a;
    --box-red-light: #d41e2a;
    --damask-tone: #b5131c;
    --silver: #e4e4e8;
    --silver-dark: #a7a7ad;
    --label-grey: #d1d1d5;
    --product-gold: #9a8660;
    --product-dark: #3b3428;
    --fold-line: rgba(0,0,0,0.18);
  }
  html, body {
    margin: 0;
    width: 1200px;
    height: 900px;
    overflow: hidden;
    background: var(--backdrop);
  }
  .canvas {
    position: relative;
    width: 1200px;
    height: 900px;
  }
  .box-net {
    position: absolute;
    left: 0;
    top: 0;
  }
  .brand-name {
    font-family: "Cinzel", serif;
    font-weight: 500;
    fill: var(--silver);
  }
</style>
</head>
<body>
<main class="canvas">
  <svg class="box-net" width="1200" height="900" viewBox="0 0 1200 900" xmlns="http://www.w3.org/2000/svg">
    <defs>
      <radialGradient id="damaskTop" cx="0.5" cy="0.45" r="0.75">
        <stop offset="0" stop-color="var(--box-red-light)"/>
        <stop offset="0.55" stop-color="var(--box-red)"/>
        <stop offset="1" stop-color="var(--damask-tone)"/>
      </radialGradient>
      <radialGradient id="damaskFront" cx="0.5" cy="0.35" r="0.8">
        <stop offset="0" stop-color="var(--box-red)"/>
        <stop offset="0.6" stop-color="var(--damask-tone)"/>
        <stop offset="1" stop-color="var(--box-red-deep)"/>
      </radialGradient>
      <linearGradient id="productTone" x1="0" y1="0" x2="1" y2="0">
        <stop offset="0" stop-color="var(--product-gold)"/>
        <stop offset="0.5" stop-color="var(--product-dark)"/>
        <stop offset="1" stop-color="var(--product-gold)"/>
      </linearGradient>
      <linearGradient id="foilFrame" x1="0" y1="0" x2="1" y2="1">
        <stop offset="0" stop-color="var(--silver)"/>
        <stop offset="0.5" stop-color="var(--silver-dark)"/>
        <stop offset="1" stop-color="var(--silver)"/>
      </linearGradient>
    </defs>

    <!-- Top panel with window -->
    <g class="panel-top" transform="translate(60 190)">
      <rect class="panel-base" width="780" height="297" fill="url(#damaskTop)" role="img" aria-label="Red panel covered in a tonal red damask flourish pattern"/>
      <g class="window" transform="translate(160 22)">
        <path class="window-frame" d="M18 0 H442 A18 18 0 0 0 460 18 V166 A18 18 0 0 0 442 184 H18 A18 18 0 0 0 0 166 V18 A18 18 0 0 0 18 0 Z" fill="url(#foilFrame)"/>
        <rect class="window-opening" x="16" y="10" width="428" height="164" fill="url(#productTone)" role="img" aria-label="Aged silver cross-shaped guitar part seen through the window"/>
      </g>
      <text class="brand-name" x="390" y="252" font-size="30" text-anchor="middle" letter-spacing="1">Hollow Marigold</text>
    </g>

    <!-- Front panel with brand mark -->
    <g class="panel-front" transform="translate(60 487)">
      <rect class="panel-base" width="780" height="186" fill="url(#damaskFront)" role="img" aria-label="Red panel covered in a tonal red damask flourish pattern"/>
      <line x1="0" y1="0" x2="780" y2="0" stroke="var(--fold-line)" stroke-width="2"/>
      <g class="brand-mark">
        <circle class="brand-dot" cx="390" cy="58" r="22" fill="var(--silver)"/>
        <text class="brand-name" x="390" y="132" font-size="34" text-anchor="middle" letter-spacing="1">Hollow Marigold</text>
      </g>
    </g>

    <!-- Side panel with sticker area -->
    <g class="panel-side" transform="translate(840 487)">
      <rect class="panel-base" width="297" height="186" fill="var(--box-red-deep)"/>
      <line x1="0" y1="0" x2="0" y2="186" stroke="var(--fold-line)" stroke-width="2"/>
      <rect class="sticker-area" x="22" y="20" width="253" height="146" fill="var(--label-grey)"/>
    </g>
  </svg>
</main>
</body>
</html>
```